Course Syllabus Template for LMG

We need a nice course syllabus created. The first page should be a cover page that includes our logo, website, and a nice picture of of a K12 teacher working with students. We've uploaded an example that artists can use if needed. The subsequent pages should just have header/footer saved that look nice and consistent throughout the rest of the document. On the subsequent pages, they don't need to have too much design but should include our website and potentially our logo or color scheme.

Additionally, we've attached a current syllabus so you can see what our current product is. In the syllabus, we have a spacer that separates the different sections of the syllabus. Ideally, we'd like a couple design options that we could use as spacers instead of the large green block that we currently use.

Full list of Items:
- Cover page (including logo, website & photo)
- template header/footer for subsequent pages that includes website, potentially logo and color scheme.
- Spacer to divide the sections of the syllabus.
- File must be in word.doc format

*We attached a PDF of a competitors syllabus that we like and thought would be a good point of reference.

Company Website is www.brightlanelearning.example.

Once completed, we would enter in all the text that is necessary for each specific course onto the syllabus template.

Target Market(s)

K12 Educators & Teachers

Colors

Designer to choose colors to be used in the design.

Requirements
Must have
• Items listed in Project dsign

```html
<!DOCTYPE html>
<html lang="en">
<head>
<meta charset="utf-8">
<title>LMG Course Syllabus Template</title>
<link href="https://fonts.googleapis.com/css2?family=Bebas+Neue&family=Arimo:ital,wght@0,400;0,700;1,400&display=swap" rel="stylesheet">
<style>
:root{
  --backdrop:#8e8f91;
  --paper:#ffffff;
  --band:#f3f3f3;
  --green:#8cc63f;
  --ink:#3a3a3a;
  --ink-soft:#6b6b6b;
  --pill:#8a8b8d;
  --pink:#e8207a;
  --purple:#7a3b97;
}
*{box-sizing:border-box;margin:0;padding:0}
html,body{width:1200px;height:1127px;overflow:hidden}
body{background:var(--backdrop);font-family:'Arimo',Arial,sans-serif;color:var(--ink);position:relative}
.page{position:absolute;width:363px;height:512px;background:var(--paper);box-shadow:2px 3px 6px rgba(0,0,0,.35);overflow:hidden}
.p1{left:37px;top:40px}.p2{left:419px;top:40px}.p3{left:796px;top:40px}
.p4{left:237px;top:584px}.p5{left:616px;top:584px}

.page-header{height:46px;background:var(--band);display:flex;justify-content:space-between;align-items:center;padding:0 12px 0 19px}
.page-header .doc-name{font-size:8.4px;line-height:11px;color:var(--ink-soft)}
.brand{display:flex;align-items:center;gap:5px;font-family:'Bebas Neue',sans-serif;color:var(--green);font-size:22px;line-height:1}
.brand .dot{width:18px;height:18px;border-radius:50%;border:2.5px solid var(--green)}

.page-footer{position:absolute;left:0;right:0;bottom:8px;height:16px}
.page-footer .rule{position:absolute;top:5px;height:6px;width:66px}
.page-footer .rule.left{left:0}.page-footer .rule.right{right:0}
.rule i{display:block;height:2px;margin-bottom:2px}
.rule i.g{background:var(--pill)}.rule i.gr{background:var(--green);height:3px}
.page-footer .pill{position:absolute;left:63px;right:63px;top:0;height:16px;border-radius:8px;background:var(--pill);color:#fff;font-size:8px;letter-spacing:.6px;text-align:center;line-height:16px}

.content{padding:16px 19px 0 19px;font-size:8.2px;line-height:10.4px}
.h-green{font-family:'Bebas Neue',sans-serif;color:var(--green);font-size:21px;line-height:21px;font-weight:400}
.h-gray{font-family:'Bebas Neue',sans-serif;color:var(--ink-soft);font-size:21px;line-height:21px;font-weight:400}
p{margin-bottom:8px}
ol{padding-left:12px}
.small{font-size:5.4px;line-height:7px;font-style:italic}

/* cover */
.cover-photo{height:245px;background:linear-gradient(135deg,#c9a27a 0%,#8d5a3b 40%,#d9c2a2 70%,#f2ead8 100%)}
.cover-tag{position:absolute;top:226px;left:0;right:0;height:36px}
.cover-tag .pill{position:absolute;left:73px;width:217px;top:0;height:36px;border-radius:18px;background:var(--green);color:#fff;font-family:'Bebas Neue',sans-serif;font-size:30px;line-height:37px;text-align:center}
.cover-tag .bar{position:absolute;top:12px;height:10px;width:60px}
.cover-tag .bar.left{left:0}.cover-tag .bar.right{right:0}
.cover-brand{position:absolute;top:300px;left:0;right:0;display:flex;justify-content:center;align-items:center;gap:10px;font-family:'Bebas Neue',sans-serif;color:var(--green);font-size:60px;line-height:1}
.cover-brand .dot{width:52px;height:52px;border-radius:50%;border:6px solid var(--green)}
.cover-title{position:absolute;top:395px;left:0;right:0;text-align:center;font-family:'Bebas Neue',sans-serif;font-size:32px;line-height:29px;font-weight:400}
.cover-title .l1{color:var(--green)}.cover-title .l2{color:var(--ink-soft)}
.cover-footer .pill{left:87px;right:87px;height:20px;line-height:20px;border-radius:10px;font-size:10px;letter-spacing:.4px}
.cover-footer{height:20px;bottom:8px}
.cover-footer .rule{width:80px}

/* syllabus */
.def{display:flex;gap:9px;margin-bottom:9px;font-size:6.9px;line-height:8.8px}
.def .ic{flex:0 0 19px;height:19px;border-radius:50%;display:flex;align-items:center;justify-content:center}
.def b.pink{color:var(--pink)}.def b.purple{color:var(--purple)}.def b.green{color:var(--green)}
.task{font-size:6.9px;line-height:8.8px}
.task ol{padding-left:14px}.task li{margin-bottom:7px}
.task li::marker{color:var(--green)}
.task ol ol{list-style:lower-alpha;padding-left:14px;margin-top:2px}
.task ol ol li{margin-bottom:0}
.task ol.roman{list-style:lower-roman;padding-left:24px}

.spacer{display:flex;align-items:center;justify-content:center;margin:14px 0}
.spacer .ln{width:90px;height:5px;border-top:1px solid var(--pill);border-bottom:2px solid var(--green)}
.spacer .ln.r{border-top:2px solid var(--green);border-bottom:1px solid var(--pill)}
.spacer .knot{width:13px;height:13px;border-radius:50%;border:2px solid var(--green);margin:0 3px}

.rows{width:100%;border-collapse:collapse;font-size:6.4px;line-height:8px}
.rows td.n{text-align:right}
.grade-scale,.rubric{width:100%;border-collapse:collapse;font-size:6px;line-height:7.3px}
.grade-scale td{border:1px solid #777;text-align:center;width:20%}
.rubric th{background:var(--green);color:#fff;text-align:left;padding:1px 3px;font-weight:700}
.rubric td{border:1px solid #999;padding:1px 3px;vertical-align:top}
.rubric td:first-child{width:52px}
.sub{font-size:10px;color:var(--ink);margin-bottom:6px;display:block}
</style>
</head>
<body>

<section class="page p1">
  <div class="cover-photo" role="img" aria-label="Photo of a smiling K12 teacher helping two young students with their schoolwork at a desk"></div>
  <div class="cover-tag">
    <div class="bar left"><div class="rule"><i class="g"></i><i class="gr"></i></div></div>
    <div class="pill">Course Syllabus</div>
    <div class="bar right"><div class="rule"><i class="g"></i><i class="gr"></i></div></div>
  </div>
  <div class="cover-brand"><span class="dot"></span>LMG</div>
  <h1 class="cover-title"><span class="l1">Growth Mindset</span><br><span class="l2">In the Classroom</span></h1>
  <footer class="page-footer cover-footer">
    <div class="rule left"><i class="g"></i><i class="gr"></i></div>
    <div class="pill">www.brightlanelearning.example</div>
    <div class="rule right"><i class="g"></i><i class="gr"></i></div>
  </footer>
</section>

<section class="page p2">
  <header class="page-header"><div class="doc-name">Course Syllabus –<br>Growth MindsetIn The Classroom</div><div class="brand"><span class="dot"></span>LMG</div></header>
  <div class="content">
    <h2 class="h-gray" style="margin-top:18px">Westridge State University —</h2>
    <h2 class="h-green" style="margin-bottom:14px">Riverton: ED 501 — 3 Semester Hours</h2>
    <p>Thank you for registering for this course. Included are the following important documents:</p>
    <ol style="margin-bottom:8px;padding-left:22px">
      <li>Course Syllabus</li><li>Assignment Plan – Assignments to turn in &amp; Grading Rubric</li><li>Course Hourly Breakdown</li><li>Participant Evaluation Form</li>
    </ol>
    <p><b>Assignment Deadline:</b> This course is a rolling course throughout the year. Your assignments are due 6 months from your registration date but can be submitted whenever completed. Please allow 4 weeks from the date assignments are submitted for the grade to be added to your transcript.</p>
    <p>Please email completed assignments in one email to admin@brightlanelearning.example.</p>
    <div style="margin-top:26px">
      <p class="small" style="margin-bottom:0"><b style="font-size:6.6px">WSU-Riverton Policies</b></p>
      <p class="small">This University complies with federal disability law and related state requirements, and no qualified student shall be denied the benefits of an education because of a disability. Students with a documented disability that may affect their work in this class, and who may need accommodations, should contact the Disability Resource Office as early as possible so that arrangements can be made in good time. To receive accommodations, students must be registered with the office and provide current documentation of their disability. The Disability Resource Office is located in the Library and Learning Commons building, on the second floor.</p>
      <p class="small">Academic dishonesty is any form of cheating that gives or receives unauthorized help in an academic exercise, or receiving credit for work that is not your own. In cases of academic dishonesty, the instructor will inform the chair of the department before any action is taken. Academic dishonesty is grounds for disciplinary action by both the instructor and the Dean of Student Services. Any student judged to have acted dishonestly may receive a failing grade for the work in question, a failing grade for the course, or any lesser penalty the instructor finds appropriate. To dispute a finding, the student should first meet with the instructor. If the dispute remains unresolved, the student may then state the case to the department chair, or to the dean if the chair is the instructor of the course. Academic dishonesty is also a behavioral matter, not only an academic one, and is therefore subject to the University disciplinary process described in the Student Code of Conduct. Whether or not any penalty has been applied, a report of the incident should be sent to the Dean of Student Services, who may begin further action. A student may appeal a grade through the Academic Appeals Board, and the decision of the Dean may be appealed through the same process.</p>
    </div>
  </div>
  <footer class="page-footer"><div class="rule left"><i class="g"></i><i class="gr"></i></div><div class="pill">555-010-2040 &nbsp;|&nbsp; www.brightlanelearning.example</div><div class="rule right"><i class="g"></i><i class="gr"></i></div></footer>
</section>

<section class="page p3">
  <header class="page-header"><div class="doc-name">Course Syllabus –<br>Growth MindsetIn The Classroom</div><div class="brand"><span class="dot"></span>LMG</div></header>
  <div class="content">
    <h2 class="h-green" style="margin-top:2px">Growth Mindset - Syllabus</h2>
    <div style="font-size:9.5px;line-height:11px;margin-bottom:12px">ED501<br>3 credits</div>
    <div class="def"><span class="ic" style="background:var(--pink)"><svg width="10" height="10" viewBox="0 0 10 10"><path d="M1 3l4-2 4 2-4 2z M3 4.5v2.5c1 1 3 1 4 0V4.5" fill="none" stroke="#fff" stroke-width="1"/></svg></span><div><b class="pink">Learning Objective:</b> Students will be able to explain how they will apply the growth mindset in their classrooms.</div></div>
    <div class="def"><span class="ic" style="background:var(--purple)"><svg width="10" height="10" viewBox="0 0 10 10"><path d="M5 1l4 2v4l-4 2-4-2V3z M1 3l4 2 4-2 M5 5v4" fill="none" stroke="#fff" stroke-width="1"/></svg></span><div><b class="purple">Fixed Mindset:</b> The thought process is that one is either smart or dumb, either good at something or not, and there is no changing that. People are born with natural talent or are born naturally smart. People's traits are fixed.</div></div>
    <div class="def"><span class="ic" style="background:var(--green)"><svg width="10" height="10" viewBox="0 0 10 10"><circle cx="5" cy="4" r="3" fill="none" stroke="#fff" stroke-width="1"/><path d="M4 7.5h2M4 9h2" stroke="#fff" stroke-width="1"/></svg></span><div><b class="green">Growth Mindset:</b> The thought process is that anyone can become smarter or better at something as long as they work at it. Effort is the means for success and intelligence. The drive is an inherent desire to learn and become better, instead of the reward or the grade.</div></div>
    <div class="task" style="margin-top:14px">
      <b style="display:block;margin-bottom:8px">Assignment</b>
      <ol>
        <li>Using the descriptions above, write one page explaining which mindset you consider yourself to have in your daily life outside of work and which mindset you consider yourself to have as a teacher. Are your mindsets different or the same in and out of the classroom? Why do you think that is? Use specific examples that you have experienced to support your choice.</li>
        <li>Read the packet entitled "Chapter 5: Families, Teachers, and Mentors—How Learning Beliefs Take Shape" from the book The Learning Stance: A New Look at Growth by Dana Whitfield.</li>
        <li>Write two pages explaining how you can use the growth mindset in your classroom. Use the following questions to guide your thinking. Use examples from the text to help you as well.
          <ol><li>What does it look like and/or sound like?</li><li>What is the teacher doing?</li><li>What are the students doing?</li><li>What do you already do that falls under the growth mindset?</li><li>What would you like to try to help you have the growth mindset?</li><li>What could you have the students do so they can have the growth mindset about their own education?</li></ol>
        </li>
      </ol>
    </div>
  </div>
  <footer class="page-footer"><div class="rule left"><i class="g"></i><i class="gr"></i></div><div class="pill">555-010-2040 &nbsp;|&nbsp; www.brightlanelearning.example</div><div class="rule right"><i class="g"></i><i class="gr"></i></div></footer>
</section>

<section class="page p4">
  <header class="page-header"><div class="doc-name">Course Syllabus –<br>Growth MindsetIn The Classroom</div><div class="brand"><span class="dot"></span>LMG</div></header>
  <div class="content" style="padding-top:8px">
    <div class="task">
      <ol start="4"><li>Final Reflection: Follow the guidelines below.
        <ol><li>For two weeks (60 hours), consistently plan and incorporate in your classroom the growth mindset as the teacher. Have your students utilize the growth mindset in your lessons as well. After each day reflect on the effectiveness of using the growth mindset.</li>
        <li>Write a two-page paper explaining:
          <ol class="roman"><li>What strategies did you utilize and why?</li><li>What went well and did you notice a difference in your students compared to in the past?</li><li>What did you do to support the effectiveness of the strategies?</li><li>What was challenging or didn't work as well as you would have hoped?</li><li>How would you modify these strategies to make them more effective in the future?</li></ol>
        </li></ol>
      </li></ol>
      <p style="padding-left:24px;font-size:6.2px;line-height:7.8px">*To view additional resources on this topic, you can visit https://brightlanelearning.example/k12resources</p>
    </div>
    <div class="spacer" style="margin:10px 0"><span class="ln"></span><span class="knot"></span><span class="ln r"></span></div>
    <h2 class="h-green" style="margin-top:10px">Growth Mindset - Assignment Plan</h2>
    <span class="sub">Grading Rubric for ED501 “Growth Mindset”</span>
    <table class="rows" style="font-size:6.2px;line-height:7.4px;margin-bottom:7px">
      <tr><td>Fixed vs. Growth Mindset Reflection (Written response rubric)</td><td class="n">X/10pts</td></tr>
      <tr><td>Growth Mindset in the Classroom (Written response rubric)</td><td class="n">X/10pts</td></tr>
      <tr><td>Final Reflection on Growth Mindset (Written response rubric)</td><td class="n">X/20 pts</td></tr>
      <tr><td style="text-align:right;padding-right:40px"><b>Final Grade</b></td><td class="n">X/40 pts</td></tr>
    </table>
    <div style="font-size:6.2px;margin-bottom:2px">Final Grade Scale</div>
    <table class="grade-scale" style="margin-bottom:6px"><tr><td>36+<br>A</td><td>32-35<br>B</td><td>28-31<br>C</td><td>24-27<br>D</td><td>23 &amp; Below<br>F</td></tr></table>
    <table class="rubric">
      <tr><th>Grade</th><th>Description</th></tr>
      <tr><td>A<br>9-10 (10)<br>18-20 (20)</td><td>Student answers all questions thoroughly with detail. There are several examples provided for each question. There is a deep level of understanding of the topic.</td></tr>
      <tr><td>B<br>8 (10)<br>16-17 (20)</td><td>Student answers all questions. There are one or two examples for each question. Student shows understanding of the topic.</td></tr>
      <tr><td>C<br>7 (10)<br>14-15 (20)</td><td>Some questions are complete while others are not. Student may have left out examples or just failed to answer all parts of the question. A correct description of the topic is used but full understanding is missing.</td></tr>
      <tr><td>D<br>6 (10)<br>12-14 (20)</td><td>Student has attempted to answer all questions but answers are incomplete. Not all parts of the questions are addressed and some or all questions are missing examples.</td></tr>
      <tr><td>F<br>5-0 (10)<br>11-0 (20)</td><td>Answers are incomplete with a one or two sentence answer. There is no elaboration and there are no examples included.</td></tr>
    </table>
  </div>
  <footer class="page-footer"><div class="rule left"><i class="g"></i><i class="gr"></i></div><div class="pill">555-010-2040 &nbsp;|&nbsp; www.brightlanelearning.example</div><div class="rule right"><i class="g"></i><i class="gr"></i></div></footer>
</section>

<section class="page p5">
  <header class="page-header"><div class="doc-name">Course Syllabus –<br>Growth MindsetIn The Classroom</div><div class="brand"><span class="dot"></span>LMG</div></header>
  <div class="content">
    <h2 class="h-green" style="margin-top:2px;margin-bottom:10px">Growth Mindset - Estimated Hour Breakdown</h2>
    <table class="rows" style="font-size:8.4px;line-height:10.4px">
      <tr><td>Reading/reviewing assigned course materials</td><td class="n">3</td></tr>
      <tr><td>Researching additional techniques</td><td class="n">2</td></tr>
      <tr><td>Planning strategies into lessons</td><td class="n">10</td></tr>
      <tr><td>Practicing strategies/techniques in the classroom</td><td class="n">60 (20)</td></tr>
      <tr><td>Reflecting on lessons and effectiveness of strategies</td><td class="n">5</td></tr>
      <tr><td>Brainstorming, researching and writing final assignments</td><td class="n">5</td></tr>
      <tr><td style="text-align:right;padding-right:20px;padding-top:10px"><b>Total Hours</b></td><td class="n" style="padding-top:10px"><b>45</b></td></tr>
    </table>
    <div class="spacer" style="margin:22px 0 28px"><span class="ln"></span><span class="knot"></span><span class="ln r"></span></div>
    <h2 class="h-green" style="margin-bottom:12px">Growth Mindset — Items to Submit</h2>
    <table class="rows" style="font-size:8.4px;line-height:10.4px;margin-bottom:10px">
      <tr><td>Fixed vs. Growth Mindset Reflection (Written response rubric)</td><td class="n">X/10pts</td></tr>
      <tr><td>Growth Mindset in the Classroom (Written response rubric)</td><td class="n">X/10pts</td></tr>
      <tr><td>Final Reflection on Growth Mindset (Written response rubric)</td><td class="n">X/20pts</td></tr>
    </table>
    <p style="font-size:8.4px;line-height:10.4px;margin-bottom:10px">Hour Log (Not Graded)</p>
    <p style="font-size:8.4px;line-height:10.4px;margin-bottom:10px">Course Evaluation (Not Graded)</p>
    <p style="font-size:8.4px;line-height:10.4px">Please submit all materials together in one email to<br>admin@brightlanelearning.example.</p>
  </div>
  <footer class="page-footer"><div class="rule left"><i class="g"></i><i class="gr"></i></div><div class="pill">555-010-2040 &nbsp;|&nbsp; www.brightlanelearning.example</div><div class="rule right"><i class="g"></i><i class="gr"></i></div></footer>
</section>

</body>
</html>
```